Bright Fern Custom Homes business card. Double sided. Modern. professional

Bright Fern Custom Homes
contemporary modern design with our logo /
Double sided with all our contact information
Use same Green colors as in our Logo. Contemporary logo that grabs your attention. Visually pleasing and balanced. Easy to read, and Vibrant. Would love an option for rounded edges. Embossed logo would be amazing.
Contact Information for Business Card
Dana Welk Owner / General Contractor Bright Fern Custom Homes p: 704.552.1830 m: 912.648.2071 e: brightferncustomhomes@mailbox.example w: www.brightferncustomhomes.example 218 Pryor Meadow Lane Alder Springs, SC 29041

```html
<!DOCTYPE html>
<html lang="en">
<head>
<meta charset="utf-8">
<title>Bright Fern Custom Homes – Business Card</title>
<link href="https://fonts.googleapis.com/css2?family=Jost:wght@400;500&family=Tinos:wght@700&display=swap" rel="stylesheet">
<style>
  :root {
    --fern-green: #5f7d2c;
    --ink: #1e1e1e;
    --text-grey: #3a3a3a;
    --card-light: #ffffff;
    --card-mint: #e6f4f1;
    --page: #f2f2f2;
  }
  * { margin: 0; padding: 0; box-sizing: border-box; }
  html, body {
    width: 1053px; height: 1200px; overflow: hidden;
    background: var(--page);
    font-family: "Jost", sans-serif;
  }
  .canvas { position: relative; width: 1053px; height: 1200px; }
  .card {
    position: absolute; left: 117px; width: 819px; height: 468px;
    border-radius: 23px;
    background: radial-gradient(ellipse at 35% 35%, var(--card-light) 0%, #f6fbfa 45%, var(--card-mint) 100%);
    box-shadow: 0 2px 10px rgba(0,0,0,0.10);
  }
  .card--front { top: 125px; }
  .card--back { top: 607px; background: radial-gradient(ellipse at 50% 40%, var(--card-light) 0%, #f6fbfa 50%, var(--card-mint) 100%); }

  .brand {
    position: absolute; display: flex; flex-direction: column; align-items: center;
    color: var(--fern-green); font-weight: 400; text-transform: uppercase; text-align: center;
  }
  .brand__dot { width: 64px; height: 64px; border-radius: 50%; background: var(--fern-green); margin-bottom: 46px; }
  .brand__main { font-size: 38px; letter-spacing: 3px; line-height: 40px; }
  .brand__sub { font-size: 11px; letter-spacing: 8px; line-height: 14px; margin-top: 2px; padding-left: 8px; }
  .card--front .brand { left: 40px; width: 356px; top: 186px; }
  .card--back .brand { left: 0; width: 819px; top: 190px; }

  .divider {
    position: absolute; left: 410px; top: 121px; width: 2px; height: 226px;
    background: linear-gradient(to bottom, transparent, var(--fern-green) 20%, var(--fern-green) 80%, transparent);
  }
  .details { position: absolute; left: 438px; top: 92px; }
  .details__name {
    font-family: "Tinos", serif; font-weight: 700; font-size: 32px;
    color: var(--fern-green); line-height: 1;
  }
  .details__role { margin-top: 10px; font-size: 21px; line-height: 27px; color: var(--text-grey); }
  .details__role .lead { color: var(--ink); }
  .contacts { list-style: none; margin-top: 22px; }
  .contacts li { display: flex; align-items: center; height: 30px; margin-bottom: 14px; font-size: 15.5px; color: var(--ink); }
  .contacts li:last-child { margin-bottom: 0; }
  .icon {
    width: 30px; height: 30px; border-radius: 3px; background: var(--fern-green);
    display: flex; align-items: center; justify-content: center; margin-right: 14px; flex: none;
  }
  .icon svg { width: 18px; height: 18px; }
  .address {
    position: absolute; left: 0; width: 819px; top: 411px;
    text-align: center; font-size: 16px; color: var(--fern-green);
  }
</style>
</head>
<body>
<main class="canvas">
  <section class="card card--front">
    <div class="brand"><span class="brand__dot"></span><span class="brand__main">Bright Fern</span><span class="brand__sub">Custom Homes</span></div>
    <div class="divider"></div>
    <div class="details">
      <h1 class="details__name">Dana Welk</h1>
      <p class="details__role"><span class="lead">Owner</span> / General Contractor<br>Bright Fern Custom Homes</p>
      <ul class="contacts">
        <li><span class="icon"><svg viewBox="0 0 24 24" fill="#fff"><path d="M6.6 10.8a15.1 15.1 0 0 0 6.6 6.6l2.2-2.2c.3-.3.7-.4 1-.2 1.1.4 2.3.6 3.6.6.6 0 1 .4 1 1V20c0 .6-.4 1-1 1C10.6 21 3 13.4 3 4c0-.6.4-1 1-1h3.5c.6 0 1 .4 1 1 0 1.3.2 2.5.6 3.6.1.3 0 .7-.2 1z"/></svg></span>704.552.1830</li>
        <li><span class="icon"><svg viewBox="0 0 24 24" fill="none" stroke="#fff" stroke-width="1.8"><rect x="7" y="2.5" width="10" height="19" rx="1.5"/><line x1="11" y1="18.5" x2="13" y2="18.5"/></svg></span>912.648.2071</li>
        <li><span class="icon"><svg viewBox="0 0 24 24" fill="none" stroke="#fff" stroke-width="1.6"><rect x="3" y="5.5" width="18" height="13"/><path d="M3 5.5l9 7 9-7M3 18.5l7-6M21 18.5l-7-6"/></svg></span>brightferncustomhomes@mailbox.example</li>
        <li><span class="icon"><svg viewBox="0 0 24 24" fill="none" stroke="#fff" stroke-width="1.4"><circle cx="12" cy="12" r="9"/><ellipse cx="12" cy="12" rx="4" ry="9"/><path d="M3 12h18M4.5 7.5h15M4.5 16.5h15"/></svg></span>www.brightferncustomhomes.example</li>
      </ul>
    </div>
    <p class="address">218 Pryor Meadow Lane Alder Springs, SC 29041</p>
  </section>

  <section class="card card--back">
    <div class="brand"><span class="brand__dot"></span><span class="brand__main">Bright Fern</span><span class="brand__sub">Custom Homes</span></div>
  </section>
</main>
</body>
</html>
```